Copper Hollow Sparkling

Hi all,

Thanks for taking the time to check out our brief.

Copper Hollow is an Australian wine company based in Victoria, and have been around for more than 20 years. We have a well-known sparkling Chardonnay Pinot Noir that needs a package revamp and we need your help!

Check out our current package here: http://www.copperhollowvino.com.au/our-wines/dsp-default_b.cfm?loadref=17

So here's the brief:

1. Use of the Copper Hollow logo (silhouette) and text mandatory - but can be as small/large as required.

2. Design must be shown on a sparkling bottle.

3. Can be closed with cork or crown seal - neck label/hood not mandatory.

4. Front label size to be no larger than 75mm high x 100mm wide. Back label to be no larger than 75mm x 100mm

5. Label does not have to be square/rectangular. Happy to see thoughts outside the box.

6. Design cannot be printed onto the bottle - must be on a label that can be applied to the bottle.

7. Be forward thinking. Be interesting. This design does not have to tie into our still (red and white) wine range.

8. Mandatory information to be shown on front label - a. Wine of Australia - b. Sparkling Chardonnay Pinot Noir

9. Mandatory info for front label - a. 750mL - b. Alcohol e.g. 13.5% ALC/VOL - c. Wine of Australi - d. Producer address (please insert dummy address at this stage - e. standard drinks e.g. approx 8.0 standard drinks (this can also be shown in the standard drinks glass logo) - f. space for a tasting blurb

10. Try to stay away from anything floral or overly girly.

Industry/Entity Type

Floral

Requirements
Must have
• Design must be shown on a sparkling wine bottle & include the full label design separately
Should not have
• Try to stay away from anything too floral and overly girly.

```html
<!DOCTYPE html>
<html lang="en">
<head>
<meta charset="utf-8">
<title>Copper Hollow Sparkling – Label on Bottle</title>
<link rel="stylesheet" href="https://fonts.googleapis.com/css2?family=Cinzel:wght@500&family=Great+Vibes&family=Roboto+Condensed:wght@400;500&display=swap">
<style>
  :root {
    --backdrop: #58585a;
    --foil: #2a2a2b;
    --foil-shade: #1f1f20;
    --glass-white: #e9e995;
    --glass-white-shade: #d9d886;
    --glass-rose: #cf4127;
    --glass-rose-shade: #b83a24;
    --label-paper: #ffffff;
    --gold: #c9a227;
    --gold-light: #e8cf6a;
    --ink: #3a3a3a;
    --fine-ink: #b89a3c;
  }
  * { margin: 0; padding: 0; box-sizing: border-box; }
  html, body { width: 900px; height: 1200px; overflow: hidden; }
  body { background: var(--backdrop); position: relative; }

  .bottle {
    position: absolute;
    top: 120px;
    width: 250px;
    height: 960px;
  }
  .bottle--white { left: 150px; --liquid: var(--glass-white); --liquid-shade: var(--glass-white-shade); }
  .bottle--rose  { left: 500px; --liquid: var(--glass-rose);  --liquid-shade: var(--glass-rose-shade); }

  .bottle__art { position: absolute; inset: 0; width: 250px; height: 960px; }
  .bottle__glass { fill: var(--liquid); }
  .bottle__glass-shade { fill: var(--liquid-shade); }
  .bottle__foil { fill: var(--foil); }
  .bottle__foil-ring { fill: var(--foil-shade); }
  .bottle__shadow { fill: #2e2e2f; }
  .label__paper { fill: var(--label-paper); stroke: var(--gold); stroke-width: 4; }
  .label__inner-frame { fill: none; stroke: var(--gold-light); stroke-width: 1; }
  .label__rule { stroke: var(--gold); stroke-width: 0.8; }
  .label__volume-ring { fill: none; stroke: var(--gold); stroke-width: 0.8; }

  .label__text {
    position: absolute;
    left: 0;
    width: 250px;
    text-align: center;
    white-space: nowrap;
  }
  .label__producer {
    top: 650px;
    font-family: "Cinzel", serif;
    font-weight: 500;
    font-size: 9px;
    letter-spacing: 2px;
    color: var(--ink);
  }
  .label__origin {
    top: 663px;
    font-family: "Great Vibes", cursive;
    font-size: 31px;
    line-height: 1;
    color: var(--gold);
  }
  .label__varietal {
    top: 707px;
    font-family: "Roboto Condensed", sans-serif;
    font-weight: 500;
    font-size: 8.6px;
    letter-spacing: 0.9px;
    color: var(--ink);
  }
  .label__address {
    top: 723px;
    font-family: "Roboto Condensed", sans-serif;
    font-size: 4.6px;
    color: var(--fine-ink);
  }
  .label__volume {
    top: 743px;
    left: 178px;
    width: 24px;
    font-family: "Roboto Condensed", sans-serif;
    font-size: 6px;
    color: var(--ink);
  }
  .label__fine {
    top: 740px;
    width: 60px;
    font-family: "Roboto Condensed", sans-serif;
    font-size: 4.2px;
    color: var(--fine-ink);
  }
  .label__fine--alcohol { left: 28px; }
  .label__fine--drinks { left: 168px; top: 756px; }
</style>
</head>
<body>

<div class="bottle bottle--white">
  <svg class="bottle__art" viewBox="0 0 250 960" role="img" aria-label="Sparkling wine bottle, pale yellow glass with black foil">
    <ellipse class="bottle__shadow" cx="125" cy="957" rx="110" ry="6"/>
    <path class="bottle__glass" d="M82,20 L82,300 C82,420 5,470 5,565 L5,910 Q5,952 45,955 L205,955 Q245,952 245,910 L245,565 C245,470 168,420 168,300 L168,20 Z"/>
    <path class="bottle__glass-shade" d="M200,470 C230,500 245,530 245,565 L245,910 Q245,952 205,955 L200,955 Z"/>
    <ellipse class="bottle__glass-shade" cx="125" cy="930" rx="100" ry="22"/>
    <path class="bottle__foil" d="M88,0 L162,0 Q172,0 172,12 L172,70 L168,78 L168,300 L82,300 L82,78 L78,70 L78,12 Q78,0 88,0 Z"/>
    <rect class="bottle__foil-ring" x="78" y="58" width="94" height="14" rx="4"/>
    <path class="label__paper" d="M10,700 C10,660 40,632 85,628 Q125,650 165,628 C210,632 240,660 240,700 C240,742 210,770 165,774 Q125,752 85,774 C40,770 10,742 10,700 Z"/>
    <path class="label__inner-frame" d="M17,700 C17,664 44,639 86,635 Q125,656 164,635 C206,639 233,664 233,700 C233,738 206,763 164,767 Q125,746 86,767 C44,763 17,738 17,700 Z"/>
    <line class="label__rule" x1="30" y1="704" x2="220" y2="704"/>
    <line class="label__rule" x1="40" y1="719" x2="210" y2="719"/>
    <ellipse class="label__volume-ring" cx="190" cy="747" rx="12" ry="6"/>
  </svg>
  <div class="label__text label__producer">COPPER HOLLOW</div>
  <div class="label__text label__origin">Wine of Australia</div>
  <div class="label__text label__varietal">SPARKLING CHARDONNAY PINOT NOIR</div>
  <div class="label__text label__address">This dummy address at this stage. Please don't read it. Thank you</div>
  <div class="label__text label__volume">750ml</div>
  <div class="label__text label__fine label__fine--alcohol">Alcohol 13.5% Vol</div>
  <div class="label__text label__fine label__fine--drinks">Approx 8.0 Std Drinks</div>
</div>

<div class="bottle bottle--rose">
  <svg class="bottle__art" viewBox="0 0 250 960" role="img" aria-label="Sparkling wine bottle, rosé red glass with black foil">
    <ellipse class="bottle__shadow" cx="125" cy="957" rx="110" ry="6"/>
    <path class="bottle__glass" d="M82,20 L82,300 C82,420 5,470 5,565 L5,910 Q5,952 45,955 L205,955 Q245,952 245,910 L245,565 C245,470 168,420 168,300 L168,20 Z"/>
    <path class="bottle__glass-shade" d="M200,470 C230,500 245,530 245,565 L245,910 Q245,952 205,955 L200,955 Z"/>
    <ellipse class="bottle__glass-shade" cx="125" cy="930" rx="100" ry="22"/>
    <path class="bottle__foil" d="M88,0 L162,0 Q172,0 172,12 L172,70 L168,78 L168,300 L82,300 L82,78 L78,70 L78,12 Q78,0 88,0 Z"/>
    <rect class="bottle__foil-ring" x="78" y="58" width="94" height="14" rx="4"/>
    <path class="label__paper" d="M10,700 C10,660 40,632 85,628 Q125,650 165,628 C210,632 240,660 240,700 C240,742 210,770 165,774 Q125,752 85,774 C40,770 10,742 10,700 Z"/>
    <path class="label__inner-frame" d="M17,700 C17,664 44,639 86,635 Q125,656 164,635 C206,639 233,664 233,700 C233,738 206,763 164,767 Q125,746 86,767 C44,763 17,738 17,700 Z"/>
    <line class="label__rule" x1="30" y1="704" x2="220" y2="704"/>
    <line class="label__rule" x1="40" y1="719" x2="210" y2="719"/>
    <ellipse class="label__volume-ring" cx="190" cy="747" rx="12" ry="6"/>
  </svg>
  <div class="label__text label__producer">COPPER HOLLOW</div>
  <div class="label__text label__origin">Wine of Australia</div>
  <div class="label__text label__varietal">SPARKLING CHARDONNAY PINOT NOIR</div>
  <div class="label__text label__address">This dummy address at this stage. Please don't read it. Thank you</div>
  <div class="label__text label__volume">750ml</div>
  <div class="label__text label__fine label__fine--alcohol">Alcohol 13.5% Vol</div>
  <div class="label__text label__fine label__fine--drinks">Approx 8.0 Std Drinks</div>
</div>

</body>
</html>
```